I am looking for help designing my new business cards. I would like rounded edges and a raised logo on the back of the card. I have 2 Logos. One with a boat in it and one without. I'd like the one on the back to be the one that includes the boat and just the name on the front. I have included multiple formats of my logo. Please let me know if you need anymore.

Target Market(s)

Potential buyers and other sales brokers

Industry/Entity Type

Sales - Yacht / Boat Sales

Contact Information for Business Card

Id liike the front to include just the business name portion of the logo along with my name (Corwin Dalby), phone number (555.318.6027), website address (www.dalbymarineco.example) and not my physical address but just "Port Lanier, SC". The back should include my full logo that has the boat included. This portion I'd prefer raised amd take up the majority of the space there. Thanks!!

Colors
0054AA
0677BA
7BADD7
CADEEF
E8F1F8
0094D4
00A9DD
6FCCEA
C7EBF8
E9F6FB

Requirements
Must have
• Double sided
Nice to have
• My email address: Corwin@dalbymarineco.example The NMTG logo somewhere small on the front of the card
Should not have
• My full address, prefer only "Port Lanier, SC"

```html
<!DOCTYPE html>
<html lang="en">
<head>
<meta charset="utf-8">
<title>Dalby Marine Co — Business Cards</title>
<link rel="stylesheet" href="https://fonts.googleapis.com/css2?family=Lato:wght@400;900&display=swap">
<style>
  :root {
    --navy: #0a2a6e;
    --brand-blue: #0054aa;
    --sky: #0677ba;
    --bright: #0094d4;
    --paper: #ffffff;
    --ink-grey: #5b5f66;
    --backdrop: #2b2d31;
  }
  * { margin: 0; padding: 0; box-sizing: border-box; }
  html, body { width: 1200px; height: 952px; overflow: hidden; }
  body {
    background: var(--backdrop);
    font-family: "Lato", sans-serif;
    display: flex;
    flex-direction: column;
    align-items: center;
    justify-content: center;
    gap: 46px;
  }
  .card {
    position: relative;
    width: 740px;
    height: 423px;
    background: var(--paper);
    border-radius: 34px;
    overflow: hidden;
  }
  .card .band { position: absolute; inset: 0; width: 100%; height: 100%; }

  .wordmark {
    position: absolute;
    display: flex;
    align-items: center;
    color: var(--navy);
    font-weight: 900;
    text-transform: uppercase;
    line-height: 1;
    white-space: nowrap;
    letter-spacing: 1px;
  }
  .wordmark .dot {
    flex: none;
    background: var(--bright);
    border-radius: 50%;
  }

  /* front */
  .front .wordmark { left: 58px; top: 58px; gap: 12px; font-size: 38px; }
  .front .wordmark .dot { width: 14px; height: 14px; }
  .contact {
    position: absolute;
    left: 392px;
    top: 150px;
    color: var(--ink-grey);
  }
  .contact .name {
    color: var(--navy);
    font-weight: 900;
    font-size: 30px;
    letter-spacing: 0.5px;
    text-transform: uppercase;
  }
  .contact .role { font-size: 18px; margin-top: 2px; }
  .contact .rule {
    width: 70px; height: 3px;
    background: var(--sky);
    margin: 12px 0 14px;
  }
  .contact ul { list-style: none; }
  .contact li {
    display: flex;
    align-items: center;
    gap: 10px;
    font-size: 18px;
    margin-bottom: 7px;
    white-space: nowrap;
  }
  .contact .icon { width: 22px; height: 22px; flex: none; }

  /* back */
  .back .wordmark { left: 260px; top: 160px; gap: 14px; font-size: 44px; }
  .back .wordmark .dot { width: 18px; height: 18px; }
</style>
</head>
<body>

  <section class="card front" aria-label="Front of card">
    <svg class="band" viewBox="0 0 740 423" preserveAspectRatio="none" role="img" aria-label="Decorative curved band in navy and blue">
      <defs>
        <linearGradient id="band-front" x1="0" y1="0" x2="1" y2="1">
          <stop offset="0" stop-color="var(--sky)"/>
          <stop offset="1" stop-color="var(--navy)"/>
        </linearGradient>
      </defs>
      <path d="M0,170 C160,160 250,300 400,423 L0,423 Z" fill="url(#band-front)"/>
    </svg>
    <div class="wordmark"><span class="dot"></span>Dalby Marine Co</div>
    <div class="contact">
      <p class="name">Corwin Dalby</p>
      <p class="role">Managing Director</p>
      <div class="rule"></div>
      <ul>
        <li>
          <svg class="icon" viewBox="0 0 22 22" aria-hidden="true"><rect width="22" height="22" rx="4" fill="var(--sky)"/><path d="M7,5 L9.5,5 L10.5,8.5 L9,9.8 C9.8,11.6 10.6,12.4 12.2,13.2 L13.5,11.7 L17,12.7 L17,15.2 C17,16 16.2,16.6 15.4,16.5 C10.2,16 6,11.8 5.5,6.6 C5.4,5.8 6.1,5 7,5 Z" fill="#fff"/></svg>
          555.318.6027
        </li>
        <li>
          <svg class="icon" viewBox="0 0 22 22" aria-hidden="true"><rect width="22" height="22" rx="4" fill="var(--sky)"/><rect x="4.5" y="6.5" width="13" height="9" fill="none" stroke="#fff" stroke-width="1.5"/><path d="M4.5,6.5 L11,11.5 L17.5,6.5" fill="none" stroke="#fff" stroke-width="1.5"/></svg>
          Corwin@dalbymarineco.example
        </li>
        <li>
          <svg class="icon" viewBox="0 0 22 22" aria-hidden="true"><rect width="22" height="22" rx="4" fill="var(--sky)"/><path d="M6,6 L17,10 L12,12 L10,17 Z" fill="#fff"/></svg>
          www.dalbymarineco.example
        </li>
        <li>
          <svg class="icon" viewBox="0 0 22 22" aria-hidden="true"><rect width="22" height="22" rx="4" fill="var(--sky)"/><path d="M11,4.5 C8.2,4.5 6.5,6.5 6.5,8.8 C6.5,12 11,17.5 11,17.5 C11,17.5 15.5,12 15.5,8.8 C15.5,6.5 13.8,4.5 11,4.5 Z" fill="#fff"/><circle cx="11" cy="8.8" r="1.8" fill="var(--sky)"/></svg>
          Port Lanier, SC
        </li>
      </ul>
    </div>
  </section>

  <section class="card back" aria-label="Back of card">
    <svg class="band" viewBox="0 0 740 423" preserveAspectRatio="none" role="img" aria-label="Decorative curved band in navy and blue">
      <defs>
        <linearGradient id="band-back" x1="0" y1="0" x2="1" y2="1">
          <stop offset="0" stop-color="var(--sky)"/>
          <stop offset="1" stop-color="var(--navy)"/>
        </linearGradient>
      </defs>
      <path d="M0,120 C150,115 300,330 560,423 L0,423 Z" fill="url(#band-back)"/>
    </svg>
    <div class="wordmark"><span class="dot"></span>Dalby Marine Co</div>
  </section>

</body>
</html>
```